Laura Brennick - Powerpoint slides

I am an educator and lecturer - I use powerpoint slides for my presentations. I would like to use my current logo and branding to create personalised powerpoint presentations.

I need a file with so I can select my personalized Powerpoint slides: I would like 3 colour variations of the following slides (design and layout is the same for all colours, with just the colour shades change)
1. Title Slide
2. Title & Content
3. Section Header
4. 2 content slide
5. Blank Slide

Note on colours: 3+ variations would be great - suggest background colours to be Turqoise
Dark/Grey Charcoal \
White
PLUS one free choice colour scheme from the designers.

Target Market(s)

Physiotherapists
Yoga Teachers
Students (yoga students and physiotherapy students)
Medical Professionals

Industry/Entity Type

Health And Wellness

Font styles to use
Serif
Sans Serif

Colors
33b8a4
876aae
0255a3

Requirements
Must have
• See the slide types in the brief description.
• Each slide should stay pretty much in the same colour, just different intensity of the shade.
• Please use the designs from my uploaded files.
• 3+ different colour variations for the regular content for slides
Nice to have
• Background patterns over part of the screen.
Should not have
• Not too many colour variations - I have chosen the ones I like as examples.

```html
<!DOCTYPE html>
<html lang="en">
<head>
<meta charset="utf-8">
<title>Laura Brennick – Title Slide Variations</title>
<link href="https://fonts.googleapis.com/css2?family=Poiret+One&family=Josefin+Sans:wght@300&display=swap" rel="stylesheet">
<style>
  :root {
    --page-bg: #ffffff;
    --teal: #167e78;
    --teal-motif: #3fa9a6;
    --violet: #846aa8;
    --violet-motif: #a58cc2;
    --blue: #0d56a0;
    --blue-motif: #4787c8;
    --ink: #ffffff;
  }
  * { margin: 0; padding: 0; box-sizing: border-box; }
  html, body {
    width: 1200px;
    height: 2250px;
    overflow: hidden;
    background: var(--page-bg);
  }
  .slide-sheet {
    position: relative;
    width: 1200px;
    height: 2250px;
  }
  .slide {
    position: absolute;
    left: 288px;
    width: 624px;
    height: 351px;
    overflow: hidden;
    color: var(--ink);
  }
  .slide--teal { background: var(--teal); --motif: var(--teal-motif); }
  .slide--violet { background: var(--violet); --motif: var(--violet-motif); }
  .slide--blue { background: var(--blue); --motif: var(--blue-motif); }

  .slide:nth-child(1) { top: 12px; }
  .slide:nth-child(2) { top: 387px; }
  .slide:nth-child(3) { top: 762px; }
  .slide:nth-child(4) { top: 1137px; }
  .slide:nth-child(5) { top: 1512px; }
  .slide:nth-child(6) { top: 1887px; }

  .motif {
    position: absolute;
    border-radius: 50%;
    background: radial-gradient(circle, transparent 30%, var(--motif) 31%, var(--motif) 42%, transparent 43%, transparent 55%, var(--motif) 56%, var(--motif) 66%, transparent 67%);
    opacity: 0.85;
  }
  .slide--corner-top .motif {
    left: -110px;
    top: -210px;
    width: 430px;
    height: 430px;
  }
  .slide--corner-bottom .motif {
    left: 290px;
    top: 115px;
    width: 340px;
    height: 340px;
  }

  .brand {
    position: absolute;
    display: flex;
    align-items: center;
    gap: 7px;
    font-family: "Poiret One", sans-serif;
    font-size: 17px;
    line-height: 1;
    color: var(--ink);
    white-space: nowrap;
  }
  .brand__dot {
    width: 14px;
    height: 14px;
    border: 1.5px solid var(--ink);
    border-radius: 50%;
  }
  .slide--corner-top .brand { right: 22px; top: 50px; }
  .slide--corner-bottom .brand { left: 30px; top: 53px; }

  .slide__title {
    position: absolute;
    font-family: "Poiret One", sans-serif;
    font-weight: 400;
    font-size: 34px;
    letter-spacing: 0.3px;
    white-space: nowrap;
  }
  .slide__subtitle {
    position: absolute;
    font-family: "Josefin Sans", sans-serif;
    font-weight: 300;
    font-size: 9.5px;
    white-space: nowrap;
  }
  .slide--corner-top .slide__title { left: 24px; top: 236px; }
  .slide--corner-top .slide__subtitle { left: 25px; top: 286px; }
  .slide--corner-bottom .slide__title { left: 18px; top: 196px; }
  .slide--corner-bottom .slide__subtitle { left: 19px; top: 246px; }
</style>
</head>
<body>
<main class="slide-sheet">
  <section class="slide slide--teal slide--corner-top">
    <div class="motif" role="img" aria-label="Faint lotus scroll ornament in lighter teal"></div>
    <div class="brand"><span class="brand__dot"></span>Laura Brennick</div>
    <h1 class="slide__title">Your Title Goes Here</h1>
    <p class="slide__subtitle">Your Subtitle Goes Here</p>
  </section>
  <section class="slide slide--violet slide--corner-top">
    <div class="motif" role="img" aria-label="Faint lotus scroll ornament in lighter violet"></div>
    <div class="brand"><span class="brand__dot"></span>Laura Brennick</div>
    <h1 class="slide__title">Your Title Goes Here</h1>
    <p class="slide__subtitle">Your Subtitle Goes Here</p>
  </section>
  <section class="slide slide--blue slide--corner-top">
    <div class="motif" role="img" aria-label="Faint lotus scroll ornament in lighter blue"></div>
    <div class="brand"><span class="brand__dot"></span>Laura Brennick</div>
    <h1 class="slide__title">Your Title Goes Here</h1>
    <p class="slide__subtitle">Your Subtitle Goes Here</p>
  </section>
  <section class="slide slide--teal slide--corner-bottom">
    <div class="motif" role="img" aria-label="Faint lotus scroll ornament in lighter teal"></div>
    <div class="brand"><span class="brand__dot"></span>Laura Brennick</div>
    <h1 class="slide__title">Your Title Goes Here</h1>
    <p class="slide__subtitle">Your Subtitle Goes Here</p>
  </section>
  <section class="slide slide--violet slide--corner-bottom">
    <div class="motif" role="img" aria-label="Faint lotus scroll ornament in lighter violet"></div>
    <div class="brand"><span class="brand__dot"></span>Laura Brennick</div>
    <h1 class="slide__title">Your Title Goes Here</h1>
    <p class="slide__subtitle">Your Subtitle Goes Here</p>
  </section>
  <section class="slide slide--blue slide--corner-bottom">
    <div class="motif" role="img" aria-label="Faint lotus scroll ornament in lighter blue"></div>
    <div class="brand"><span class="brand__dot"></span>Laura Brennick</div>
    <h1 class="slide__title">Your Title Goes Here</h1>
    <p class="slide__subtitle">Your Subtitle Goes Here</p>
  </section>
</main>
</body>
</html>
```